New Business Card Design for a Payroll Concierge Company

I need a new business card design that is simple and includes my current information. I am a payroll concierge company that processes payroll for clients who employ household employees and I also manage my client's personal bills, financial records. I want to include my current logo and a logo for an association (PFHKT) I belong too on the front of my business card. I will include both my all my company logo files and the association logo files.

Target Market(s)

People who hire household employees, nannies, home health aides, butlers, maids, etc for wealthy individuals and senior citizens who need help in the home.

Industry/Entity Type

Financial Service

Contact Information for Business Card

Company logo

Name: Martin L. Vellacourt
Managing Director

Office number: 203-555-0148
Business Cell: 203-555-0173

Website: www.tallywagedesk.net
Email: Martin.Vellacourt@tallywagedesk.com

Company address:

17 Heron Lane
Suite 208
Wilton,CT 06412

Font styles to use
Serif
Sans Serif

Colors
3176b5
85cae6
cee9f5
33a6d7
d3d3d3
dbdbdb

Requirements
Must have
• I need to have my company logo and name, phone numbers, website, email, and address on the card. I also want the association logo on the card somewhere but not too big. Small enough to see the logo maybe on the top or bottom corner. Or some where on there card that it doesn't take away the design.
Nice to have
• i like the blue color in my logo, grey, please see must haves business card details.
Should not have
• PLEASE DO NOT USE THE BUSINESS CARD DESIGNS IN THE FILES I UPLOADED. I AM NOT INTERESTED IN THAT DESIGN. ALSO THE ADDRESS AND WEBSITE ARE INCORRECT ON THOSE DESIGNS. PLEASE USE THE UPDATED INFO ON BUSINESS CARD DETAILS

```html
<!DOCTYPE html>
<html lang="en">
<head>
<meta charset="utf-8">
<title>Tally Wage Desk — Business Card</title>
<link href="https://fonts.googleapis.com/css2?family=Arimo:wght@400;700&display=swap" rel="stylesheet">
<style>
  :root {
    --stage: #262626;
    --card-white: #f7f7f6;
    --brand-blue: #2f74c0;
    --back-blue: #3a7fcb;
    --back-blue-deep: #2f6fb9;
    --badge-blue: #85cae6;
    --ink: #3a3a3a;
    --rule: #d3d3d3;
  }
  * { box-sizing: border-box; margin: 0; padding: 0; }
  html, body {
    width: 1200px;
    height: 974px;
    overflow: hidden;
    background: var(--stage);
    font-family: "Arimo", Arial, sans-serif;
  }
  .canvas {
    position: relative;
    width: 1200px;
    height: 974px;
  }
  .card {
    position: absolute;
    top: 195px;
    width: 340px;
    height: 584px;
    border-radius: 24px;
    overflow: hidden;
    box-shadow: 0 18px 40px rgba(0,0,0,0.45);
  }
  .card--front {
    left: 235px;
    background: var(--card-white);
    text-align: center;
    color: var(--ink);
  }
  .card--back {
    left: 625px;
    background: linear-gradient(160deg, var(--back-blue), var(--back-blue-deep));
  }
  .brand {
    margin-top: 96px;
    display: flex;
    justify-content: center;
    align-items: center;
    gap: 9px;
  }
  .brand__mark {
    width: 18px;
    height: 18px;
    background: var(--brand-blue);
  }
  .brand__name {
    font-weight: 700;
    font-size: 25px;
    letter-spacing: 0.4px;
    color: var(--brand-blue);
    white-space: nowrap;
  }
  .person {
    margin-top: 140px;
  }
  .person__name {
    font-weight: 700;
    font-size: 20px;
    color: var(--brand-blue);
    letter-spacing: 0.3px;
  }
  .person__title {
    margin-top: 6px;
    font-size: 15px;
  }
  .rule {
    width: 86px;
    height: 1px;
    background: var(--rule);
    margin: 30px auto 26px;
  }
  .contact {
    font-size: 14.5px;
    line-height: 21px;
  }
  .contact__label {
    font-weight: 700;
    color: var(--brand-blue);
  }
  .contact__sep { margin: 0 6px; }
  .address {
    font-size: 15px;
    line-height: 22px;
  }
  .association-badge {
    position: absolute;
    right: 22px;
    bottom: 20px;
    width: 28px;
    height: 28px;
    border-radius: 50%;
    background: var(--badge-blue);
  }
</style>
</head>
<body>
<main class="canvas">
  <section class="card card--front">
    <div class="brand">
      <span class="brand__mark"></span>
      <span class="brand__name">TALLY WAGE DESK</span>
    </div>

    <div class="person">
      <p class="person__name">MARTIN L. VELLACOURT</p>
      <p class="person__title">Managing Director</p>
    </div>

    <div class="rule"></div>

    <div class="contact">
      <p><span class="contact__label">M:</span> 203-555-0173<span class="contact__sep">|</span><span class="contact__label">T:</span> 203-555-0148</p>
      <p>Martin.Vellacourt@tallywagedesk.com</p>
      <p>www.tallywagedesk.net</p>
    </div>

    <div class="rule"></div>

    <div class="address">
      <p>17 Heron Lane, Suite 208</p>
      <p>Wilton,CT 06412</p>
    </div>

    <span class="association-badge" role="img" aria-label="Association membership badge"></span>
  </section>

  <section class="card card--back" role="img" aria-label="Card back: blue field with a repeating spot-gloss company mark pattern and a large central mark"></section>
</main>
</body>
</html>
```